Mortgage Broking boutique Business

I’m wanting a revamped look to my existing business card design. I do like the black and silver but happy to have other colours introduced based on your creation. I’ve attached a copy of my current card so you can have a starting point updated details noted brloe. I deal with high net worth individuals so need my card to be sophisticated, classy that gives off a classy vibe

Target Market(s)

High net worth, wealthy

Industry/Entity Type

Mortgage Brokerage

Contact Information for Business Card

Job title: Finance Executive
Phone: +61 7 3287 4419
Mobile: 0471 352 608
Email: marcus@quillbrookcapital.com.au
Web: www.quillbrookcapital.com.au
Address: level 36 Tindale Court, 58 Harwick St Brisbane QLD 4000

Font styles to use
Other font styles liked:
• Helvetica

Colors

Designer to choose colors to be used in the design.

Requirements
Must have
• Use my existing card design as a starting point

```html
<!DOCTYPE html>
<html lang="en">
<head>
<meta charset="utf-8">
<title>Quillbrook Capital – Business Card</title>
<link rel="stylesheet" href="https://fonts.googleapis.com/css2?family=Jost:wght@300&family=Arimo:wght@400&display=swap">
<style>
  :root {
    --stage: #e4e6e8;
    --card: #050505;
    --silver-light: #f4f4f4;
    --silver-mid: #a9a9a9;
    --silver-dark: #3e3e3e;
    --text-light: #ededed;
    --text-muted: #c8c8c8;
  }
  html, body {
    margin: 0;
    width: 1200px;
    height: 1200px;
    overflow: hidden;
    background: var(--stage);
  }
  .canvas { position: relative; width: 1200px; height: 1200px; }

  .card {
    position: absolute;
    width: 720px;
    background: var(--card);
    border-radius: 30px 68px 30px 68px;
    overflow: hidden;
    box-shadow: 0 18px 40px rgba(0,0,0,0.18);
  }
  .card--front { left: 240px; top: 132px; height: 400px; }
  .card--back  { left: 236px; top: 687px; height: 393px; }

  .brand {
    position: absolute;
    font-family: "Jost", sans-serif;
    font-weight: 300;
    color: var(--text-light);
    text-transform: uppercase;
    text-align: center;
    white-space: nowrap;
  }
  .brand--front { left: 176px; width: 400px; top: 126px; }
  .brand__main  { display: block; font-size: 25px; letter-spacing: 5px; line-height: 32px; }
  .brand__sub   { display: block; font-size: 16px; letter-spacing: 4px; line-height: 22px; }
  .brand--back {
    left: 0; right: 0;
    top: 63px;
    font-size: 18px;
    letter-spacing: 5px;
    color: var(--text-muted);
  }

  .silver-band {
    position: absolute;
    left: 0; right: 0;
    top: 321px;
    height: 27px;
    background: linear-gradient(180deg, var(--silver-dark) 0%, var(--silver-light) 38%, var(--silver-mid) 62%, var(--silver-dark) 100%);
  }
  .silver-band__url {
    position: absolute;
    left: 0; right: 0;
    top: 323px;
    text-align: center;
    font-family: "Arimo", sans-serif;
    font-size: 20px;
    line-height: 24px;
    color: #ffffff;
    text-shadow: 0 1px 2px #000;
  }

  .name-plate {
    position: absolute;
    left: 234px;
    top: 130px;
    width: 220px;
    height: 80px;
    box-sizing: border-box;
    border: 3px solid var(--silver-mid);
    border-radius: 40px;
    text-align: center;
    font-family: "Arimo", sans-serif;
    color: var(--text-light);
  }
  .name-plate__name  { margin-top: 11px; font-size: 19px; line-height: 24px; text-transform: uppercase; }
  .name-plate__title { font-size: 17px; line-height: 22px; }

  .connectors { position: absolute; left: 0; top: 0; }

  .contact {
    position: absolute;
    font-family: "Arimo", sans-serif;
    font-size: 13px;
    line-height: 14px;
    color: var(--text-muted);
    white-space: nowrap;
  }
  .contact--left  { text-align: right; }
</style>
</head>
<body>
<main class="canvas">

  <section class="card card--front" aria-label="Card front">
    <div class="brand brand--front">
      <span class="brand__main">Quillbrook</span>
      <span class="brand__sub">Capital</span>
    </div>
    <div class="silver-band"></div>
    <div class="silver-band__url">www.quillbrookcapital.com.au</div>
  </section>

  <section class="card card--back" aria-label="Card back">
    <div class="brand brand--back">Quillbrook.Capital</div>

    <div class="name-plate">
      <div class="name-plate__name">Marcus Avery</div>
      <div class="name-plate__title">Finance Executive</div>
    </div>

    <svg class="connectors" width="720" height="393" viewBox="0 0 720 393" aria-hidden="true">
      <defs>
        <linearGradient id="wire" x1="0" y1="0" x2="1" y2="0">
          <stop offset="0" stop-color="#555"/>
          <stop offset="0.5" stop-color="#f0f0f0"/>
          <stop offset="1" stop-color="#555"/>
        </linearGradient>
      </defs>
      <g fill="url(#wire)">
        <rect x="282" y="217" width="4" height="71"/>
        <rect x="308" y="217" width="4" height="93"/>
        <rect x="334" y="217" width="4" height="116"/>
        <rect x="359" y="217" width="4" height="93"/>
        <rect x="386" y="217" width="4" height="71"/>
      </g>
      <g fill="#c4c4c4" stroke="#6a6a6a" stroke-width="1.5">
        <circle cx="284" cy="288" r="5"/>
        <circle cx="310" cy="310" r="5"/>
        <circle cx="336" cy="333" r="5"/>
        <circle cx="361" cy="310" r="5"/>
        <circle cx="388" cy="288" r="5"/>
      </g>
    </svg>

    <div class="contact contact--left" style="right:449px; top:281px">0471 352 608</div>
    <div class="contact contact--left" style="right:420px; top:303px">marcus@quillbrookcapital.com.au</div>
    <div class="contact contact--left" style="right:398px; top:327px">www.quillbrookcapital.com.au</div>

    <div class="contact" style="left:400px; top:281px">+61 7 3287 4419</div>
    <div class="contact" style="left:375px; top:304px">Level 36 Tindale Court,</div>
    <div class="contact" style="left:375px; top:327px">58 Harwick St Brisbane QLD 4000</div>
  </section>

</main>
</body>
</html>
```